Brightpath Home & Upkeep Services, are a company that offers a 'one stop shop' pre-move clean up a

I have already selected a logo which I would like on the front of the business cards along with phone numbers, web address and email which are:
0419586402
www.brightpathhome.com.au
brightpathandupkeep@mailnest.com

On the back of the card I would like to list some of the types of service we offer (clean - move - repairs/maintenance) which are:
CLEAN - windows, gutters, solar panels, driveways/paths, carpets.
MOVE - Small/medium size house/office moves, large item pick-up & delivery, yard clean-up and removal.
General maintenance and repairs.

I would like the blue logo on a gray background.

Thanks

```html
<!DOCTYPE html>
<html lang="en">
<head>
<meta charset="utf-8">
<title>Brightpath Home &amp; Upkeep Services – Business Cards</title>
<link rel="stylesheet" href="https://fonts.googleapis.com/css2?family=Open+Sans:wght@400;600;700&display=swap">
<style>
  :root {
    --page: #d9dadc;
    --brand-blue: #2466b3;
    --brand-blue-deep: #1c5499;
    --card-white: #f4f5f6;
    --bar-white: #ffffff;
    --label-blue: #5b93cf;
    --text-white: #ffffff;
  }
  * { margin: 0; padding: 0; box-sizing: border-box; }
  html, body { width: 1200px; height: 874px; overflow: hidden; }
  body {
    background: var(--page);
    font-family: "Open Sans", Arial, sans-serif;
    position: relative;
  }

  .card {
    position: absolute;
    overflow: hidden;
    border-radius: 4px;
    box-shadow: 0 6px 22px rgba(0,0,0,0.18);
  }

  /* Services card (portrait) */
  .card--services {
    left: 120px; top: 137px;
    width: 360px; height: 600px;
    background: var(--card-white);
  }
  .services-panel {
    position: absolute; left: 0; top: 0;
    width: 100%; height: 480px;
    background: var(--brand-blue);
    padding-top: 46px;
  }
  .service-heading {
    display: block;
    background: var(--bar-white);
    color: var(--label-blue);
    font-size: 17px;
    font-weight: 400;
    letter-spacing: 1px;
    height: 28px;
    line-height: 28px;
    padding-left: 38px;
    margin-left: 0;
  }
  .service-heading--clean { width: 300px; margin-left: 22px; padding-left: 30px; }
  .service-heading--move { width: 262px; margin-left: 22px; padding-left: 30px; margin-top: 26px; }
  .service-heading--general {
    width: 276px; margin-left: 22px; padding-left: 14px; margin-top: 26px;
    color: var(--brand-blue); font-size: 16px; letter-spacing: 0.2px;
  }
  .service-list {
    list-style: none;
    color: var(--text-white);
    font-size: 16px;
    line-height: 21px;
    margin-top: 12px;
    padding-left: 110px;
  }
  .service-list--move { padding-left: 86px; }
  .service-list li::before { content: "- "; }

  .services-brand {
    position: absolute; left: 0; bottom: 0;
    width: 100%; height: 120px;
    display: flex; align-items: center; justify-content: center; gap: 8px;
  }

  .brand-name {
    color: var(--brand-blue);
    font-weight: 700;
    font-size: 14px;
    line-height: 1.15;
  }
  .brand-mark {
    width: 14px; height: 14px;
    background: var(--brand-blue);
    flex: none;
  }

  /* Contact card (landscape content) */
  .card--contact {
    left: 540px; top: 287px;
    width: 600px; height: 360px;
    background: var(--card-white);
  }
  .contact-brand {
    position: absolute; right: 40px; top: 44px;
    display: flex; align-items: center; gap: 10px;
  }
  .contact-brand .brand-name { font-size: 22px; width: 250px; text-align: right; }
  .contact-brand .brand-mark { width: 22px; height: 22px; }

  .contact-list {
    position: absolute; left: 0; top: 170px;
    list-style: none;
  }
  .contact-bar {
    display: flex; align-items: center; gap: 12px;
    height: 30px;
    background: var(--brand-blue);
    color: var(--text-white);
    font-size: 13px;
    padding-left: 22px;
    margin-bottom: 22px;
  }
  .contact-bar--phone { width: 230px; }
  .contact-bar--email { width: 470px; }
  .contact-bar--web { width: 380px; }
  .contact-icon { width: 16px; height: 16px; flex: none; }
</style>
</head>
<body>

<section class="card card--services" aria-label="Services card">
  <div class="services-panel">
    <span class="service-heading service-heading--clean">CLEAN</span>
    <ul class="service-list service-list--clean">
      <li>Windows</li>
      <li>Gutters</li>
      <li>Solar panels</li>
      <li>Driveways/Paths</li>
      <li>Carpets</li>
    </ul>

    <span class="service-heading service-heading--move">MOVE</span>
    <ul class="service-list service-list--move">
      <li>Small/medium size house/<br>&nbsp;&nbsp;office moves</li>
      <li>large item pick-up &amp; delivery,</li>
      <li>yard clean-up and removal</li>
    </ul>

    <span class="service-heading service-heading--general">General maintenance and repairs</span>
  </div>

  <div class="services-brand">
    <span class="brand-mark"></span>
    <span class="brand-name">Brightpath Home &amp;<br>Upkeep Services</span>
  </div>
</section>

<section class="card card--contact" aria-label="Contact card">
  <div class="contact-brand">
    <span class="brand-name">Brightpath Home &amp; Upkeep Services</span>
    <span class="brand-mark"></span>
  </div>

  <ul class="contact-list">
    <li class="contact-bar contact-bar--phone">
      <svg class="contact-icon" viewBox="0 0 16 16" aria-hidden="true">
        <circle cx="8" cy="8" r="7" fill="none" stroke="#fff" stroke-width="1.2"/>
        <path d="M5.5 4.5 l1.5 0 l0.6 2 l-1 0.8 a5 5 0 0 0 2.1 2.1 l0.8 -1 l2 0.6 l0 1.5 a1 1 0 0 1 -1 1 A6 6 0 0 1 4.5 5.5 a1 1 0 0 1 1 -1z" fill="#fff"/>
      </svg>
      <span>0419586402</span>
    </li>
    <li class="contact-bar contact-bar--email">
      <svg class="contact-icon" viewBox="0 0 16 16" aria-hidden="true">
        <rect x="1.5" y="3.5" width="13" height="9" fill="none" stroke="#fff" stroke-width="1.2"/>
        <path d="M1.5 3.5 L8 9 L14.5 3.5" fill="none" stroke="#fff" stroke-width="1.2"/>
      </svg>
      <span>brightpathandupkeep@mailnest.com</span>
    </li>
    <li class="contact-bar contact-bar--web">
      <svg class="contact-icon" viewBox="0 0 16 16" aria-hidden="true">
        <path d="M8 1.5 a4.5 4.5 0 0 1 4.5 4.5 c0 3.5 -4.5 8.5 -4.5 8.5 s-4.5 -5 -4.5 -8.5 A4.5 4.5 0 0 1 8 1.5z" fill="#fff"/>
        <circle cx="8" cy="6" r="1.7" fill="#2466b3"/>
      </svg>
      <span>www.brightpathhome.com.au</span>
    </li>
  </ul>
</section>

</body>
</html>
```